Modern Business Card for Industrial Company

We need business cards updated with modern fonts and make it look more technical, sharp and clean. The logo should not be changed, but we are looking for fresh solutions for how other information on the card is laid out in an interesting way. The company provides machinery and services to the ceramic industry and deals with cutting-edge technology. The design should reflect a technologically advanced and modern company that deals with the latest European technologies.

Font styles to use
Sans Serif

Requirements
Must have
• Modern fonts, technical look and feel

```html
<!DOCTYPE html>
<html lang="en">
<head>
<meta charset="utf-8">
<title>Korvatech Business Card</title>
<link rel="stylesheet" href="https://fonts.googleapis.com/css2?family=Montserrat:wght@400;500;600;700;800&display=swap">
<style>
  :root {
    --backdrop: #e9b89a;
    --navy: #2d3360;
    --navy-deep: #262b52;
    --navy-light: #3a4072;
    --red: #8e2a30;
    --paper: #ececec;
    --paper-shade: #e2e2e4;
    --ink-blue: #2f4a8a;
    --white: #ffffff;
    --grey: #9a9ca6;
  }
  * { margin: 0; padding: 0; box-sizing: border-box; }
  html, body { width: 1200px; height: 1125px; overflow: hidden; }
  body {
    background: var(--backdrop);
    font-family: "Montserrat", Arial, sans-serif;
    position: relative;
  }
  .card {
    position: absolute;
    left: 240px;
    width: 720px;
    height: 411px;
    overflow: hidden;
    border-radius: 4px;
  }

  /* Front side */
  .card-front {
    top: 92px;
    background: linear-gradient(135deg, var(--navy-light) 0%, var(--navy) 45%, var(--navy-deep) 100%);
  }
  .front-facet { position: absolute; inset: 0; }
  .front-tab {
    position: absolute;
    right: 0;
    top: 70px;
    width: 14px;
    height: 150px;
    background: var(--red);
    border-radius: 10px 0 0 10px;
  }
  .front-wordmark {
    position: absolute;
    left: 0; right: 0;
    top: 150px;
    text-align: center;
    color: var(--white);
    font-weight: 800;
    font-size: 78px;
    letter-spacing: 4px;
    text-transform: uppercase;
  }
  .front-footer {
    position: absolute;
    right: 0;
    bottom: 0;
    width: 420px;
    height: 78px;
    background: var(--white);
    border-radius: 70px 0 0 0;
  }
  .front-web {
    position: absolute;
    right: 44px;
    bottom: 26px;
    color: var(--red);
    font-weight: 500;
    font-size: 20px;
    letter-spacing: 1.5px;
  }

  /* Back side */
  .card-back {
    top: 614px;
    background: linear-gradient(160deg, var(--white) 0%, var(--paper) 55%, var(--paper-shade) 100%);
  }
  .back-facet { position: absolute; inset: 0; }
  .name-tab {
    position: absolute;
    left: 232px;
    top: 0;
    width: 456px;
    height: 150px;
    background: var(--navy);
    border-radius: 0 0 60px 60px;
    text-align: center;
    padding-top: 42px;
  }
  .person-name {
    color: var(--white);
    font-weight: 800;
    font-size: 30px;
    letter-spacing: 3px;
    text-transform: uppercase;
  }
  .person-title {
    color: var(--red);
    font-weight: 500;
    font-size: 15px;
    letter-spacing: 12px;
    text-transform: uppercase;
    margin-top: 4px;
  }
  .contact {
    position: absolute;
    display: flex;
    align-items: flex-start;
    gap: 16px;
    color: var(--ink-blue);
    font-weight: 600;
    font-size: 14px;
    letter-spacing: 2px;
    text-transform: uppercase;
    line-height: 1.35;
  }
  .contact svg { flex: none; width: 28px; height: 28px; }
  .contact-address { left: 62px; top: 172px; }
  .contact-web { left: 62px; top: 240px; }
  .contact-email { left: 396px; top: 196px; }
  .contact-phone { left: 396px; top: 252px; }
  .contact-web, .contact-email, .contact-phone { align-items: center; }

  .bar { position: absolute; background: var(--red); }
  .bar-left { left: 0; top: 320px; width: 40px; height: 24px; }
  .bar-main { left: 206px; top: 332px; width: 384px; height: 28px; }
  .bar-right { right: 0; top: 366px; width: 50px; height: 24px; }
  .back-wordmark {
    position: absolute;
    left: 50px;
    top: 318px;
    color: var(--ink-blue);
    font-weight: 800;
    font-size: 19px;
    letter-spacing: 0.5px;
    line-height: 1.3;
    text-transform: uppercase;
  }
  .social {
    position: absolute;
    left: 516px;
    top: 368px;
    color: var(--navy);
    font-weight: 600;
    font-size: 8px;
    letter-spacing: 0.3px;
    white-space: nowrap;
    text-transform: uppercase;
  }
  .social-dots { display: flex; gap: 22px; margin-top: 7px; padding-left: 10px; }
  .social-dots span { width: 9px; height: 9px; border-radius: 50%; background: var(--red); }
</style>
</head>
<body>

<section class="card card-front" aria-label="Card front">
  <svg class="front-facet" viewBox="0 0 720 411" preserveAspectRatio="none" aria-hidden="true">
    <polygon points="420,0 720,0 720,300" fill="#ffffff" opacity="0.04"/>
    <polygon points="0,411 0,180 260,411" fill="#000000" opacity="0.06"/>
  </svg>
  <div class="front-tab"></div>
  <div class="front-wordmark">Korvatech</div>
  <div class="front-footer"></div>
  <div class="front-web">www.korvatech.com</div>
</section>

<section class="card card-back" aria-label="Card back">
  <svg class="back-facet" viewBox="0 0 720 411" preserveAspectRatio="none" aria-hidden="true">
    <polygon points="0,150 260,120 420,300 120,330" fill="#000000" opacity="0.025"/>
    <polygon points="420,300 720,200 720,411 300,411" fill="#000000" opacity="0.03"/>
  </svg>

  <div class="name-tab">
    <div class="person-name">Marco Ferrani</div>
    <div class="person-title">President</div>
  </div>

  <div class="contact contact-address">
    <svg viewBox="0 0 24 24" aria-hidden="true"><path d="M12 2a7 7 0 0 0-7 7c0 5 7 13 7 13s7-8 7-13a7 7 0 0 0-7-7z" fill="none" stroke="#8e2a30" stroke-width="2"/><circle cx="12" cy="9" r="2.6" fill="none" stroke="#8e2a30" stroke-width="2"/></svg>
    <div>418 Kiln Road, Suite 200<br>Brookfield, GA 30118</div>
  </div>
  <div class="contact contact-web">
    <svg viewBox="0 0 24 24" aria-hidden="true"><circle cx="12" cy="12" r="9.5" fill="#8e2a30"/><g fill="none" stroke="#ececec" stroke-width="1.4"><ellipse cx="12" cy="12" rx="4" ry="9.5"/><line x1="2.5" y1="12" x2="21.5" y2="12"/><line x1="12" y1="2.5" x2="12" y2="21.5"/></g></svg>
    <div>www.korvatech.com</div>
  </div>
  <div class="contact contact-email">
    <svg viewBox="0 0 24 24" aria-hidden="true"><rect x="2.5" y="5" width="19" height="14" fill="none" stroke="#8e2a30" stroke-width="2"/><path d="M2.5 5l9.5 8 9.5-8" fill="none" stroke="#8e2a30" stroke-width="2"/></svg>
    <div>mferrani@korvatech.com</div>
  </div>
  <div class="contact contact-phone">
    <svg viewBox="0 0 24 24" aria-hidden="true"><rect x="6.5" y="2" width="11" height="20" rx="1.5" fill="none" stroke="#8e2a30" stroke-width="2"/><line x1="10.5" y1="18.5" x2="13.5" y2="18.5" stroke="#8e2a30" stroke-width="2"/></svg>
    <div>404 555-0172</div>
  </div>

  <div class="bar bar-left"></div>
  <div class="back-wordmark">Korvatech</div>
  <div class="bar bar-main"></div>
  <div class="social">
    Find me on social media!
    <div class="social-dots"><span></span><span></span><span></span></div>
  </div>
  <div class="bar bar-right"></div>
</section>

</body>
</html>
```